Website Re-Design Project

We have popular voucher code website and we would like to make re-design for whole website. Including following pages: Home page, store page, listing page, article page and blog page.

Our website is: www.lumipolkuvaara.com. Its non english language but you will get the point.

Design should be clean, stylish and highly conversion. At the moment there is too much thing in homepage. Example the carusel should be removed. We want keep our main colours green and orange.

Please look our home page mockup from files. That is only one option and we are open to see different choises for the layout.

Inspirations :
http://www.pebblemarket.co.uk/
http://www.zonnewijzerhoek.nl/
http://www.harborlanternfieldguide.co.uk/

Target Market(s)

People who are looking vouchers and coupon codes for the online shops.

Industry/Entity Type

Store

Requirements
Should not have
• Any carusels

```html
<!DOCTYPE html>
<html lang="fi">
<head>
<meta charset="utf-8">
<title>Lumipolkuvaara.com – alennuskoodit</title>
<link href="https://fonts.googleapis.com/css2?family=Questrial&family=Arimo:wght@400;700&display=swap" rel="stylesheet">
<style>
:root{
  --green:#66b10f;
  --green-dark:#4f9a06;
  --green-light:#8fd33a;
  --text:#555;
  --muted:#888;
  --line:#dcdcdc;
  --band:#f2f2f2;
  --dark:#3a3839;
  --topbar:#333;
  --white:#fff;
}
*{box-sizing:border-box;margin:0;padding:0}
html,body{width:1200px;height:1000px;overflow:hidden;background:var(--white)}
body{position:relative;font-family:Arimo,Arial,sans-serif;color:var(--text)}
.abs{position:absolute}
.page{position:absolute;left:88px;width:1055px}
.topbar{top:0;height:12px;background:var(--topbar);font-size:7.5px;color:#eee}
.topbar nav{position:absolute;right:238px;top:2px;word-spacing:1px}
.topbar span{margin:0 4px;color:#aaa}
.header{top:12px;height:65px;background:var(--white)}
.brand-mark{left:345px;top:27px;width:32px;height:32px;border-radius:50%;background:var(--green)}
.brand-name{left:385px;top:29px;font-size:16px;font-weight:700;color:#222}
.brand-tag{left:386px;top:47px;font-size:7px;color:#444}
.main-nav{left:644px;top:31px;width:259px;height:26px;border-radius:5px;background:linear-gradient(#93d640,var(--green-dark));display:flex;align-items:center;font-size:8.5px;color:var(--white)}
.main-nav a{flex:auto;text-align:center;line-height:26px;border-left:1px solid rgba(0,0,0,.12);color:inherit;text-decoration:none}
.main-nav a:first-child{border-left:0}
.hero-band{top:77px;height:516px;background:var(--band)}
.headline{left:0;width:1224px;top:91px;text-align:center;font-family:Questrial,sans-serif;font-size:22px;color:var(--green-dark)}
.subhead{left:0;width:1224px;top:120px;text-align:center;font-family:Questrial,sans-serif;font-size:18px;color:#555}
.search{left:433px;top:158px;width:370px;height:41px;border-radius:7px;background:var(--green);padding:3px;display:flex}
.search-input{flex:0 0 261px;background:var(--white);border-radius:5px 0 0 5px;font-family:Questrial,sans-serif;font-size:12px;color:var(--green);line-height:35px;padding-left:12px}
.search-btn{flex:1;color:var(--white);font-family:Questrial,sans-serif;font-size:15px;line-height:35px;padding-left:18px;display:flex;align-items:center;gap:10px}
.rule{left:345px;top:219px;width:556px;height:1px;background:var(--line)}
.stores{left:345px;top:234px;display:flex;gap:8px}
.store-tile{width:86px;height:49px;background:var(--white);border:1px solid #e2e2e2;border-radius:8px;box-shadow:0 5px 5px -3px rgba(0,0,0,.12);display:flex;align-items:center;justify-content:center;font-size:10px;font-weight:700;color:#222}
.panel{top:303px;width:179px;height:215px;background:var(--white);border:1px solid #e0e0e0;box-shadow:0 4px 4px -3px rgba(0,0,0,.12)}
.panel h2{height:32px;font-family:Questrial,sans-serif;font-weight:400;font-size:14.5px;color:#555;padding:6px 9px;background:linear-gradient(var(--white),#f4f4f4);border-bottom:1px solid #eee}
.panel ul{list-style:none;padding:11px 8px 0}
.panel li{height:29.4px;position:relative;padding-left:0}
.panel li.iconed{padding-left:26px}
.item-title{display:block;font-size:8px;color:var(--green-dark);line-height:10px}
.item-sub{display:block;font-size:6.5px;color:#555;line-height:8px}
.chev{position:absolute;right:2px;top:2px}
.cat-icon{position:absolute;left:3px;top:1px;width:14px;height:12px;border-radius:2px}
.view-more{position:absolute;left:0;right:0;bottom:0;height:27px;background:#f5f5f5;text-align:right;padding-right:14px;font-size:8px;line-height:27px;color:var(--muted)}
.view-more.active{color:var(--green-dark)}
.newsletter{left:345px;top:537px;width:556px;height:49px;background:var(--white);border:1px solid #ddd;overflow:hidden}
.nl-lead{left:55px;top:18px;font-size:6.5px;font-weight:700;color:#333}
.nl-sub{left:55px;top:27px;font-size:6.5px;color:var(--green-dark)}
.nl-input{left:376px;top:15px;width:114px;height:21px;background:#f3f3f3;font-size:7px;color:#aaa;line-height:21px;padding-left:7px}
.nl-btn{left:491px;top:15px;width:46px;height:21px;background:var(--green-dark);color:var(--white);font-size:7px;font-weight:700;text-align:center;line-height:21px}
.featured{top:593px;height:106px;background:var(--white);border-top:1px solid #e4e4e4}
.featured h2{position:absolute;left:265px;top:8px;font-family:Questrial,sans-serif;font-weight:400;font-size:14px;color:#555}
.link-col{top:42px;list-style:none;font-size:7px;line-height:10px;color:#666}
.link-col .on{color:var(--green-dark)}
.info-band{top:699px;height:169px;background:var(--band);border-top:1px solid #e2e2e2}
.box{background:var(--white);border:1px solid #ddd}
.welcome{left:345px;top:706px;width:374px;height:148px;padding:9px 8px}
.box h2{font-family:Questrial,sans-serif;font-weight:400;font-size:14px;color:#555;margin-bottom:10px}
.welcome p{font-size:6.3px;line-height:8.4px;color:#888;margin-bottom:6px}
.welcome a{color:var(--green-dark)}
.social{left:726px;top:705px;width:176px;height:149px;padding:9px 10px}
.social h2{margin-bottom:6px}
.fb-mark{left:14px;top:33px;width:26px;height:26px;border-radius:50%;background:var(--green)}
.fb-name{left:48px;top:33px;font-size:7px;font-weight:700;color:#3b5998}
.fb-like{left:48px;top:43px;width:36px;height:11px;border:1px solid #bbb;background:#eef;font-size:6px;line-height:9px;text-align:center;color:#333}
.fb-count{left:14px;top:64px;font-size:6px;color:#333;border-top:1px solid #ddd;padding-top:3px;width:150px}
.fb-count b{font-weight:400;color:#3b5998}
.fans{left:14px;top:77px;display:grid;grid-template-columns:repeat(4,28px);gap:3px}
.fans div{width:28px;height:24px}
.fb-foot{left:14px;top:134px;width:150px;border-top:1px solid #ddd;padding-top:3px;font-size:5.5px;color:#333;display:flex;align-items:center;gap:3px}
.fb-foot i{display:inline-block;width:6px;height:6px;background:#3b5998}
.footer{top:868px;height:132px;background:var(--dark);color:#888}
.footer h3{font-weight:400;font-size:10px;color:var(--white)}
.f-col1{left:265px;top:23px}
.f-col1 ul{list-style:none;margin-top:12px;font-size:7px;line-height:10px}
.f-col2{left:414px;top:23px;width:200px}
.f-col2 p{margin-top:12px;font-size:7px;line-height:10px}
.f-div{top:22px;width:1px;height:98px;background:#555}
.f-logo{right:242px;top:44px;text-align:right}
.f-logo strong{display:block;font-family:Questrial,sans-serif;font-weight:400;font-size:13px;color:#aaa;margin-bottom:9px}
.f-logo small{display:block;font-size:5.5px;color:#bbb;line-height:7px}
</style>
</head>
<body>

<div class="page abs topbar">
  <nav>Blogi <span>|</span> Usein kysytyt kysymykset <span>|</span> Kerro alennuskoodista</nav>
</div>

<header class="page abs header"></header>
<div class="abs brand-mark"></div>
<div class="abs brand-name">Lumipolkuvaara.com</div>
<div class="abs brand-tag">säästä rahaa verkko-ostoksissa</div>
<nav class="abs main-nav"><a href="#">Home</a><a href="#">Top 20</a><a href="#">Latest</a><a href="#">Shops</a><a href="#">Categories</a></nav>

<section class="page abs hero-band"></section>
<h1 class="abs headline" style="font-weight:400">Find 612 active voucher codes today.</h1>
<p class="abs subhead">Harbor Lantern Voucher Codes</p>
<div class="abs search">
  <div class="search-input">Search a Store..</div>
  <div class="search-btn">Search
    <svg width="14" height="14" viewBox="0 0 14 14"><circle cx="8" cy="5.5" r="4" fill="none" stroke="#b9e58a" stroke-width="1.8"/><line x1="5" y1="8.5" x2="1.5" y2="12.5" stroke="#b9e58a" stroke-width="2.2" stroke-linecap="round"/></svg>
  </div>
</div>
<div class="abs rule"></div>

<div class="abs stores">
  <div class="store-tile">Vindra</div>
  <div class="store-tile">Lumo &amp; Co</div>
  <div class="store-tile">Saappaala</div>
  <div class="store-tile">Kulmapiste</div>
  <div class="store-tile">Matkalehti</div>
  <div class="store-tile">Vaatekaari</div>
</div>

<section class="abs panel" style="left:345px">
  <h2>Top 20</h2>
  <ul>
    <li><span class="item-title">Item One</span><span class="item-sub">Sub title goes Here</span><svg class="chev" width="6" height="14" viewBox="0 0 6 14"><path d="M1 1 L5 7 L1 13" fill="none" stroke="#66b10f" stroke-width="1.6"/></svg></li>
    <li><span class="item-title">Item Two</span><span class="item-sub">Sub title goes Here</span><svg class="chev" width="6" height="14" viewBox="0 0 6 14"><path d="M1 1 L5 7 L1 13" fill="none" stroke="#66b10f" stroke-width="1.6"/></svg></li>
    <li><span class="item-title">Item Three</span><span class="item-sub">Sub title goes Here</span><svg class="chev" width="6" height="14" viewBox="0 0 6 14"><path d="M1 1 L5 7 L1 13" fill="none" stroke="#66b10f" stroke-width="1.6"/></svg></li>
    <li><span class="item-title">Item Four</span><span class="item-sub">Sub title goes Here</span><svg class="chev" width="6" height="14" viewBox="0 0 6 14"><path d="M1 1 L5 7 L1 13" fill="none" stroke="#66b10f" stroke-width="1.6"/></svg></li>
    <li><span class="item-title">Item Five</span><span class="item-sub">Sub title goes Here</span><svg class="chev" width="6" height="14" viewBox="0 0 6 14"><path d="M1 1 L5 7 L1 13" fill="none" stroke="#66b10f" stroke-width="1.6"/></svg></li>
  </ul>
  <div class="view-more active">+ View more</div>
</section>

<section class="abs panel" style="left:534px">
  <h2>Latest</h2>
  <ul>
    <li><span class="item-title">Item One</span><span class="item-sub">Sub title goes Here</span><svg class="chev" width="6" height="14" viewBox="0 0 6 14"><path d="M1 1 L5 7 L1 13" fill="none" stroke="#66b10f" stroke-width="1.6"/></svg></li>
    <li><span class="item-title">Item Two</span><span class="item-sub">Sub title goes Here</span><svg class="chev" width="6" height="14" viewBox="0 0 6 14"><path d="M1 1 L5 7 L1 13" fill="none" stroke="#66b10f" stroke-width="1.6"/></svg></li>
    <li><span class="item-title">Item Three</span><span class="item-sub">Sub title goes Here</span><svg class="chev" width="6" height="14" viewBox="0 0 6 14"><path d="M1 1 L5 7 L1 13" fill="none" stroke="#66b10f" stroke-width="1.6"/></svg></li>
    <li><span class="item-title">Item Four</span><span class="item-sub">Sub title goes Here</span><svg class="chev" width="6" height="14" viewBox="0 0 6 14"><path d="M1 1 L5 7 L1 13" fill="none" stroke="#66b10f" stroke-width="1.6"/></svg></li>
    <li><span class="item-title">Item Five</span><span class="item-sub">Sub title goes Here</span><svg class="chev" width="6" height="14" viewBox="0 0 6 14"><path d="M1 1 L5 7 L1 13" fill="none" stroke="#66b10f" stroke-width="1.6"/></svg></li>
  </ul>
  <div class="view-more">+ View more</div>
</section>

<section class="abs panel" style="left:722px">
  <h2>Categories</h2>
  <ul>
    <li class="iconed"><span class="cat-icon" role="img" aria-label="Laptop category icon" style="background:#9fb6c8"></span><span class="item-title">Item One</span><span class="item-sub">Sub title goes Here</span><svg class="chev" width="6" height="14" viewBox="0 0 6 14"><path d="M1 1 L5 7 L1 13" fill="none" stroke="#66b10f" stroke-width="1.6"/></svg></li>
    <li class="iconed"><span class="cat-icon" role="img" aria-label="Travel category icon" style="background:#bcd7e6"></span><span class="item-title">Item Two</span><span class="item-sub">Sub title goes Here</span><svg class="chev" width="6" height="14" viewBox="0 0 6 14"><path d="M1 1 L5 7 L1 13" fill="none" stroke="#66b10f" stroke-width="1.6"/></svg></li>
    <li class="iconed"><span class="cat-icon" role="img" aria-label="Fashion category icon" style="background:#d9824a"></span><span class="item-title">Item Three</span><span class="item-sub">Sub title goes Here</span><svg class="chev" width="6" height="14" viewBox="0 0 6 14"><path d="M1 1 L5 7 L1 13" fill="none" stroke="#66b10f" stroke-width="1.6"/></svg></li>
    <li class="iconed"><span class="cat-icon" role="img" aria-label="Books category icon" style="background:#3f8a2a"></span><span class="item-title">Item Four</span><span class="item-sub">Sub title goes Here</span><svg class="chev" width="6" height="14" viewBox="0 0 6 14"><path d="M1 1 L5 7 L1 13" fill="none" stroke="#66b10f" stroke-width="1.6"/></svg></li>
    <li class="iconed"><span class="cat-icon" role="img" aria-label="Gifts category icon" style="background:#d9483b"></span><span class="item-title">Item Five</span><span class="item-sub">Sub title goes Here</span><svg class="chev" width="6" height="14" viewBox="0 0 6 14"><path d="M1 1 L5 7 L1 13" fill="none" stroke="#66b10f" stroke-width="1.6"/></svg></li>
  </ul>
  <div class="view-more">+ View more</div>
</section>

<section class="abs newsletter">
  <svg class="abs" style="left:0;top:0" width="58" height="49" viewBox="0 0 58 49">
    <path d="M0 0 H58 L0 49 Z" fill="#66b10f"/>
    <rect x="12" y="12" width="26" height="18" fill="#e8e8e8" stroke="#bbb"/>
    <path d="M12 12 L25 23 L38 12" fill="none" stroke="#999" stroke-width="1"/>
  </svg>
  <div class="abs nl-lead">Stay on top of what's happening in responsive design with responsive for your company</div>
  <div class="abs nl-sub">Sign Up to recive monthly reader</div>
  <div class="abs nl-input">Signup@example.com</div>
  <div class="abs nl-btn">Sign up</div>
</section>

<section class="page abs featured">
  <h2>Featured Stores</h2>
  <ul class="abs link-col" style="left:265px"><li class="on">Link 1</li><li>Link 2</li><li>Link 3</li><li>Link 4</li><li>Link 5</li></ul>
  <ul class="abs link-col" style="left:379px"><li>Link 1</li><li>Link 2</li><li>Link 3</li><li>Link 4</li><li>Link 5</li></ul>
  <ul class="abs link-col" style="left:492px"><li>Link 1</li><li>Link 2</li><li>Link 3</li><li>Link 4</li><li>Link 5</li></ul>
  <ul class="abs link-col" style="left:605px"><li>Link 1</li><li>Link 2</li><li>Link 3</li><li>Link 4</li><li>Link 5</li></ul>
  <ul class="abs link-col" style="left:718px"><li>Link 1</li><li>Link 2</li><li>Link 3</li><li>Link 4</li><li>Link 5</li></ul>
</section>

<section class="page abs info-band"></section>
<article class="abs box welcome">
  <h2>Welcome to our website</h2>
  <p>Lorem Ipsum is simply dummy text of the printing and typesetting industry. Lorem Ipsum has been the industry's standard dummy text ever sinceLorem Ipsum is simply dummy text of the printing and typesetting industry. Lorem Ipsum has been the industry's standard dummy text ever since</p>
  <p>Lorem Ipsum is simply dummy text of the <a href="#">printing and typesetting industry</a>. Lorem Ipsum has been the industry's standard dummy text ever since</p>
  <p>Lorem Ipsum is simply dummy text of the printing and typesetting industry. Lorem Ipsum has been the industry's standard dummy text ever sinceLorem Ipsum is simply dummy text of the printing and typesetting industry. Lorem Ipsum has been the industry's standard dummy text ever since</p>
</article>
<aside class="abs box social">
  <h2>Find Us Kuvakirja</h2>
  <div class="abs fb-mark"></div>
  <div class="abs fb-name">Lumipolkuvaara.com</div>
  <div class="abs fb-like">Tykkää</div>
  <div class="abs fb-count">5 096 henkilöä tykkää sivusta <b>Lumipolkuvaara.com</b>.</div>
  <div class="abs fans" role="img" aria-label="Profile pictures of page followers">
    <div style="background:#c9804f"></div><div style="background:#8b7a63"></div><div style="background:#6f6a70"></div><div style="background:#c79a6a"></div>
    <div style="background:#5d7ea0"></div><div style="background:#4e87b5"></div><div style="background:#9a9a9a"></div><div style="background:#7f7460"></div>
  </div>
  <div class="abs fb-foot"><i></i>Kuvakirjan sivuliitännäinen</div>
</aside>

<footer class="page abs footer">
  <div class="abs f-col1">
    <h3>Lorem Ipsum</h3>
    <ul><li>Lorem Ipsum one</li><li>Lorem Ipsum two</li><li>Lorem Ipsum three</li><li>Lorem Ipsum four</li><li>Lorem Ipsum five</li><li>Lorem Ipsum six</li></ul>
  </div>
  <div class="abs f-div" style="left:392px"></div>
  <div class="abs f-col2">
    <h3>Lorem Ipsum</h3>
    <p>Lorem Ipsum is simply dummy text of the printing and typesetting industry. Lorem Ipsum has been the industry's standard dummy text ever sinceLorem Ipsum is simply dummy text of the printing and typesetting industry. Lorem Ipsum has been the industry's standard dummy text ever since</p>
  </div>
  <div class="abs f-div" style="left:630px"></div>
  <div class="abs f-logo">
    <strong>COMPANY LOGO</strong>
    <small>2013. All right reserved</small>
  </div>
</footer>

</body>
</html>
```